Business Card for Amber Finch Advisors

Business card design for Amber Finch Advisors, a new consulting and financial advisory firm. I would like the designs to integrate the logo attached (at least on 1 side).

Target Market(s)

individual and institutional clients

Contact Information for Business Card

Daniel R. Hollis, CFA
Managing Director
amberfinchadvisors.comp
hollis@amberfinchadvisors.example
(555) 217-4630

```html
<!DOCTYPE html>
<html lang="en">
<head>
<meta charset="utf-8">
<title>Amber Finch Advisors – Business Card</title>
<link href="https://fonts.googleapis.com/css2?family=Lato:wght@400;700;900&family=Montserrat:wght@600&display=swap" rel="stylesheet">
<style>
  :root {
    --brand-blue: #00a9e8;
    --card-black: #161616;
    --band-black: #1b1b1b;
    --ink: #111111;
    --paper: #ffffff;
    --backdrop: #e9e9e9;
  }
  html, body {
    margin: 0;
    padding: 0;
    overflow: hidden;
  }
  .canvas {
    position: relative;
    width: 1200px;
    height: 586px;
    background: var(--backdrop);
    overflow: hidden;
    font-family: "Lato", sans-serif;
  }
  .card {
    position: absolute;
    top: 160px;
    width: 468px;
    height: 267px;
    overflow: hidden;
    box-shadow: 0 6px 14px rgba(0,0,0,0.18);
  }
  .card-front {
    left: 78px;
    background: var(--card-black);
    display: flex;
    align-items: center;
    justify-content: center;
  }
  .card-back {
    left: 636px;
    background: var(--paper);
  }
  .wordmark {
    font-family: "Montserrat", sans-serif;
    font-weight: 600;
    color: var(--brand-blue);
    letter-spacing: 0.04em;
    text-transform: uppercase;
    white-space: nowrap;
    margin: 0;
  }
  .card-front .wordmark {
    font-size: 27px;
  }
  .card-back .wordmark {
    position: absolute;
    top: 36px;
    left: 0;
    width: 468px;
    text-align: center;
    font-size: 19px;
  }
  .icon-tab {
    position: absolute;
    left: 0;
    top: 117px;
    width: 38px;
    height: 101px;
    background: var(--brand-blue);
    border-radius: 0 10px 10px 0;
  }
  .icon-tab svg {
    position: absolute;
    left: 10px;
    width: 17px;
    height: 17px;
  }
  .contact-list {
    position: absolute;
    left: 50px;
    top: 129px;
    margin: 0;
    padding: 0;
    list-style: none;
    font-size: 12px;
    font-weight: 700;
    color: var(--ink);
  }
  .contact-list li {
    height: 30px;
    line-height: 18px;
  }
  .person {
    position: absolute;
    right: 27px;
    top: 149px;
    text-align: right;
  }
  .person-name {
    margin: 0;
    font-size: 14.5px;
    font-weight: 900;
    color: var(--brand-blue);
  }
  .person-title {
    margin: 3px 0 0;
    font-size: 11px;
    color: var(--ink);
  }
  .footer-band {
    position: absolute;
    left: 0;
    bottom: 0;
    width: 468px;
    height: 18px;
  }
</style>
</head>
<body>
<div class="canvas">

  <section class="card card-front" aria-label="Card front">
    <p class="wordmark">Amber Finch Advisors</p>
  </section>

  <section class="card card-back" aria-label="Card back">
    <p class="wordmark">Amber Finch Advisors</p>

    <div class="icon-tab" aria-hidden="true">
      <svg style="top:8px" viewBox="0 0 24 24" fill="none" stroke="#fff" stroke-width="2" stroke-linecap="round" stroke-linejoin="round">
        <path d="M3 9c0-3 4-4 9-4s9 1 9 4l-1 2h-4l-1-2H9l-1 2H4z"/>
        <path d="M6 13l-1 7h14l-1-7z"/>
        <circle cx="12" cy="16.5" r="1.5"/>
      </svg>
      <svg style="top:42px" viewBox="0 0 24 24" fill="none" stroke="#fff" stroke-width="2" stroke-linejoin="round">
        <rect x="3" y="6" width="18" height="12"/>
        <path d="M3 6l9 7 9-7"/>
      </svg>
      <svg style="top:75px" viewBox="0 0 24 24" fill="none" stroke="#fff" stroke-width="2.2" stroke-linecap="round">
        <path d="M10 14a4 4 0 0 0 5.6 0l3-3a4 4 0 0 0-5.6-5.6l-1 1"/>
        <path d="M14 10a4 4 0 0 0-5.6 0l-3 3a4 4 0 0 0 5.6 5.6l1-1"/>
      </svg>
    </div>

    <ul class="contact-list">
      <li class="contact-phone">(555) 217-4630</li>
      <li class="contact-email">hollis@amberfinchadvisors.example</li>
      <li class="contact-web">www.amberfinchadvisors.comp</li>
    </ul>

    <div class="person">
      <p class="person-name">Daniel R. Hollis, CFA</p>
      <p class="person-title">Managing Director</p>
    </div>

    <svg class="footer-band" viewBox="0 0 468 18" preserveAspectRatio="none" aria-hidden="true">
      <polygon points="0,3 290,3 282,18 0,18" fill="var(--band-black)"/>
      <path d="M284,18 Q292,0 318,0 L468,0 L468,18 Z" fill="var(--brand-blue)"/>
    </svg>
  </section>

</div>
</body>
</html>
```